TK Joinery

Cabinet maker. Kitchens. Wardrobes. Vanitys. Entertainment units

Target Market(s)

Modern contemporary.geometry. colours black, gray, charcoal and orange. Matt card gloss letters

Industry/Entity Type

Entertainment

Contact Information for Business Card

Marcel Otvany 0417 382 594
marcel.otvany@fernmail.test
ABN 731 4928 5170

Font styles to use
Decorative

Colors
000000

Requirements
Should not have
• Pictures

```html
<!DOCTYPE html>
<html lang="en">
<head>
<meta charset="utf-8">
<title>TK Joinery — Business Card</title>
<link rel="stylesheet" href="https://fonts.googleapis.com/css2?family=Arimo:ital,wght@0,400;0,700;1,400&display=swap">
<style>
  :root {
    --orange: #e8661c;
    --orange-band: #e06016;
    --ink: #1f1f1f;
    --black: #111112;
    --charcoal: #2b2c2e;
    --charcoal-light: #3b3c3f;
    --grey: #a9acaf;
    --grey-light: #d3d5d7;
    --paper: #ffffff;
    --backdrop: #e9e7e4;
  }
  * { margin: 0; padding: 0; box-sizing: border-box; }
  html, body { width: 1200px; height: 892px; overflow: hidden; }
  body {
    background: var(--backdrop);
    font-family: "Arimo", Arial, sans-serif;
    display: flex;
    flex-direction: column;
    align-items: center;
    justify-content: center;
    gap: 44px;
  }
  .card {
    position: relative;
    width: 665px;
    height: 380px;
    overflow: hidden;
    box-shadow: 0 6px 18px rgba(0,0,0,.18);
  }

  /* Front */
  .card--front { background: var(--paper); }
  .front__name {
    position: absolute; left: 42px; top: 48px;
    font-size: 31px; color: var(--ink); letter-spacing: .5px;
  }
  .front__brand {
    position: absolute; right: 40px; top: 30px;
    font-size: 62px; color: var(--orange); letter-spacing: 1px;
  }
  .front__divider { position: absolute; left: 332px; top: 166px; }
  .front__contacts {
    position: absolute; left: 388px; top: 164px;
    list-style: none; font-size: 16px; color: var(--ink);
  }
  .front__contacts li { display: flex; align-items: center; gap: 8px; line-height: 28px; white-space: nowrap; }
  .front__contacts svg { flex: none; }
  .front__abn { padding-left: 21px; }
  .front__bands { position: absolute; left: 0; bottom: 0; }
  .front__address {
    position: absolute; left: 215px; bottom: 30px;
    font-size: 15px; color: var(--paper); letter-spacing: .3px;
  }

  /* Back */
  .card--back {
    background: linear-gradient(180deg, var(--charcoal) 0%, var(--charcoal-light) 100%);
  }
  .back__brand {
    position: absolute; left: 0; right: 0; top: 100px;
    text-align: center; font-size: 72px; color: var(--paper); letter-spacing: 1px;
  }
  .back__rule {
    position: absolute; left: 0; right: 0; top: 298px; height: 4px;
    background: var(--orange);
  }
  .back__strip {
    position: absolute; left: 0; right: 0; top: 302px; bottom: 0;
    background: var(--black);
    display: flex; align-items: center; padding: 0 24px; gap: 10px;
    white-space: nowrap;
  }
  .back__trade { font-style: italic; font-size: 24px; color: var(--orange); }
  .back__dash { color: var(--orange); font-size: 20px; margin: 0 12px; }
  .back__services { display: flex; align-items: center; gap: 7px; list-style: none; }
  .back__services li { font-weight: 700; font-size: 15.5px; color: var(--paper); display: flex; align-items: center; gap: 7px; }
  .back__services li + li::before {
    content: ""; width: 6px; height: 6px; border-radius: 50%; background: var(--orange);
  }
</style>
</head>
<body>

  <section class="card card--front" aria-label="Business card front">
    <div class="front__name">Marcel Otvany</div>
    <div class="front__brand">TK Joinery</div>

    <svg class="front__divider" width="40" height="110" viewBox="0 0 40 110" aria-hidden="true">
      <line x1="38" y1="2" x2="2" y2="108" stroke="#111" stroke-width="2"/>
    </svg>

    <ul class="front__contacts">
      <li>
        <svg width="13" height="13" viewBox="0 0 13 13" aria-hidden="true"><rect width="13" height="13" fill="#111"/><path d="M4 3 q-1 3 2 6 q2 1 3 0 l-1-1.5 -1 .5 q-1.5-1-2-2.5 l1-.7z" fill="#fff"/></svg>
        0417 382 594
      </li>
      <li>
        <svg width="13" height="13" viewBox="0 0 13 13" aria-hidden="true"><rect width="13" height="13" fill="#111"/><rect x="3" y="4" width="7" height="5" fill="none" stroke="#fff"/><path d="M3 4 l3.5 3 3.5-3" fill="none" stroke="#fff"/></svg>
        marcel.otvany@fernmail.test
      </li>
      <li>
        <svg width="13" height="13" viewBox="0 0 13 13" aria-hidden="true"><rect width="13" height="13" fill="#111"/><circle cx="6.5" cy="6.5" r="3.5" fill="none" stroke="#fff"/><line x1="3" y1="6.5" x2="10" y2="6.5" stroke="#fff"/></svg>
        www.tkjoinery.test
      </li>
      <li class="front__abn">ABN 731 4928 5170</li>
    </ul>

    <svg class="front__bands" width="665" height="82" viewBox="0 0 665 82" aria-hidden="true">
      <defs>
        <linearGradient id="greyBand" x1="0" y1="0" x2="0" y2="1">
          <stop offset="0" stop-color="#d3d5d7"/>
          <stop offset="1" stop-color="#a9acaf"/>
        </linearGradient>
      </defs>
      <rect x="0" y="0" width="665" height="82" fill="url(#greyBand)"/>
      <path d="M200 14 H665 V62 H170 L188 22 Q192 14 200 14 Z" fill="#e06016"/>
    </svg>
    <div class="front__address">4810 Larkfield Rd. Unit 22 Westbrook, CA 90417</div>
  </section>

  <section class="card card--back" aria-label="Business card back">
    <div class="back__brand">TK Joinery</div>
    <div class="back__rule"></div>
    <div class="back__strip">
      <span class="back__trade">Cabinet maker</span>
      <span class="back__dash">-</span>
      <ul class="back__services">
        <li>Kitchens</li>
        <li>Wardrobes</li>
        <li>Vanitys</li>
        <li>Entertainment units</li>
      </ul>
    </div>
  </section>

</body>
</html>
```